Banner Design for High End Jewelry Website

We need a banner for our website (brindlestone.com) for a sale that we will be running. The banner should be a size 1187 × 400. I have included a few pieces of jewelry to be included in the banner (do not need to use all, can use just some). The banner should say:
"Christmas is Closer Than You Think Sale!"
Shop Now

Industry/Entity Type

Jewelry

```html
<!DOCTYPE html>
<html lang="en">
<head>
<meta charset="utf-8">
<title>Brindlestone – Christmas Sale Banner</title>
<link rel="stylesheet" href="https://fonts.googleapis.com/css2?family=Jost:wght@400;500;600&family=Open+Sans:wght@400;600&display=swap">
<style>
  :root {
    --page: #ffffff;
    --cream: #fbf8f3;
    --gold-text: #a98b5c;
    --band: #b39266;
    --think: #d98b68;
    --shop: #fb8a66;
    --nav: #a68a70;
    --nav-text: #ffffff;
    --ink: #3a3a3a;
    --muted: #8a8a8a;
    --arrivals: #d9c6b6;
    --arrivals-dark: #7b6150;
    --tree-top: #8a6a5a;
    --tree-mid: #46582e;
    --tree-low: #6a6040;
    --piece-light: #e9d9b0;
    --piece-dark: #cdb47e;
  }
  * { box-sizing: border-box; margin: 0; padding: 0; }
  html, body { width: 1200px; height: 1000px; overflow: hidden; background: var(--page); }
  .canvas { position: relative; width: 1200px; height: 1000px; font-family: "Jost", sans-serif; }

  /* Banner (native 1185 x 400) */
  .banner { position: absolute; width: 1185px; height: 400px; }
  .banner--hero { left: 8px; top: 6px; }
  .banner--inpage { left: 115px; top: 567px; transform: scale(0.841); transform-origin: 0 0; }

  .banner__tree {
    position: absolute; left: 0; top: 0; width: 295px; height: 400px;
    background: linear-gradient(180deg, var(--tree-top) 0%, var(--tree-mid) 35%, var(--tree-mid) 65%, var(--tree-low) 100%);
  }
  .banner__panel { position: absolute; left: 295px; top: 0; width: 890px; height: 356px; background: var(--cream); }
  .banner__headline {
    position: absolute; left: 0; right: 0; top: 14px; text-align: center;
    font-size: 56px; font-weight: 500; color: var(--gold-text); letter-spacing: 0.5px; line-height: 1.2;
  }
  .banner__piece {
    position: absolute; border-radius: 14px;
    background: linear-gradient(160deg, var(--piece-light), var(--piece-dark));
  }
  .piece--earrings { left: 92px; top: 100px; width: 205px; height: 134px; }
  .piece--cluster-ring { left: 307px; top: 100px; width: 160px; height: 134px; }
  .piece--scale-ring { left: 487px; top: 100px; width: 145px; height: 134px; }
  .piece--brooch { left: 647px; top: 100px; width: 170px; height: 134px; }

  .banner__button {
    position: absolute; display: flex; align-items: center; justify-content: center;
    border-radius: 40px; color: #fff; font-weight: 600; letter-spacing: 0.5px;
  }
  .button--think { left: 43px; top: 266px; width: 224px; height: 56px; background: var(--think); font-size: 24px; }
  .button--shop { left: 559px; top: 257px; width: 290px; height: 73px; background: var(--shop); font-size: 37px; }

  .banner__band {
    position: absolute; left: 295px; top: 356px; width: 890px; height: 44px; background: var(--band);
    display: flex; align-items: center; justify-content: center;
    color: #fff; font-size: 28px; font-weight: 600;
  }

  /* Site header */
  .site-header__brand { position: absolute; left: 130px; top: 418px; width: 320px; }
  .brand__name { font-size: 50px; font-weight: 400; color: var(--ink); line-height: 1.6; }
  .brand__tagline { font-size: 15.5px; color: var(--ink); letter-spacing: 0.2px; }

  .site-search { position: absolute; left: 550px; top: 428px; width: 275px; height: 28px; border-bottom: 2px solid var(--nav); }
  .site-search__icon { position: absolute; left: 8px; top: 5px; }
  .site-search__label { position: absolute; left: 42px; top: 5px; font-family: "Open Sans", sans-serif; font-size: 10px; color: var(--muted); }
  .site-search__submit { position: absolute; right: 0; top: 2px; width: 26px; height: 26px; background: var(--nav); display: flex; align-items: center; justify-content: center; }

  .site-tools { position: absolute; top: 417px; display: flex; flex-direction: column; align-items: center; gap: 12px;
    font-family: "Open Sans", sans-serif; font-size: 9.5px; letter-spacing: 1.2px; color: var(--muted); }
  .tool--newsletter { left: 851px; }
  .tool--wishlist { left: 958px; }
  .tool--cart { left: 1044px; }

  .site-nav { position: absolute; left: 471px; top: 485px; display: flex; gap: 4px; }
  .site-nav__item { height: 40px; background: var(--nav); color: var(--nav-text); font-size: 16px; font-weight: 500;
    display: flex; align-items: center; justify-content: center; }

  /* New arrivals */
  .arrivals { position: absolute; left: 130px; top: 932px; width: 968px; height: 68px; border: 1px solid #ece6e0; border-top: none; }
  .arrivals__bar { height: 44px; background: var(--arrivals); display: flex; align-items: center; justify-content: center;
    font-family: "Open Sans", sans-serif; font-size: 22px; color: #fff; letter-spacing: 0.5px; position: relative; }
  .arrivals__view-all { position: absolute; right: 10px; top: 9px; width: 76px; height: 31px; background: var(--arrivals-dark);
    color: #e8ddd4; font-size: 11px; display: flex; align-items: center; justify-content: center; letter-spacing: -0.2px; }
</style>
</head>
<body>
<div class="canvas">

  <section class="banner banner--hero">
    <div class="banner__tree" role="img" aria-label="Photo of a lit, decorated Christmas tree by a window"></div>
    <div class="banner__panel">
      <h1 class="banner__headline">Christmas is closer</h1>
      <div class="banner__piece piece--earrings" role="img" aria-label="Product photo: pair of gemstone earrings"></div>
      <div class="banner__piece piece--cluster-ring" role="img" aria-label="Product photo: cabochon cluster ring"></div>
      <div class="banner__piece piece--scale-ring" role="img" aria-label="Product photo: textured gold band ring"></div>
      <div class="banner__piece piece--brooch" role="img" aria-label="Product photo: floral gold brooch"></div>
      <div class="banner__button button--think">THINK SALE !</div>
      <div class="banner__button button--shop">SHOP NOW</div>
    </div>
    <div class="banner__band">Thank You</div>
  </section>

  <header class="site-header">
    <div class="site-header__brand">
      <div class="brand__name">Brindlestone</div>
      <div class="brand__tagline">FINE ESTATE AND DESIGNER JEWELRY</div>
    </div>

    <div class="site-search">
      <svg class="site-search__icon" width="14" height="14" viewBox="0 0 14 14"><circle cx="6" cy="6" r="4.5" fill="none" stroke="#999" stroke-width="1.3"/><line x1="9.3" y1="9.3" x2="13" y2="13" stroke="#999" stroke-width="1.3"/></svg>
      <span class="site-search__label">Search</span>
      <span class="site-search__submit"><svg width="14" height="12" viewBox="0 0 14 12"><path d="M1 6l4 4 8-9" fill="none" stroke="#fff" stroke-width="2"/></svg></span>
    </div>

    <div class="site-tools tool--newsletter">
      <svg width="22" height="16" viewBox="0 0 22 16"><rect x="1" y="1" width="20" height="14" fill="none" stroke="#888" stroke-width="1.3"/><path d="M1 1l10 8 10-8" fill="none" stroke="#888" stroke-width="1.3"/></svg>
      <span>NEWSLETTER</span>
    </div>
    <div class="site-tools tool--wishlist">
      <svg width="22" height="19" viewBox="0 0 22 19"><path d="M11 18S1 11.5 1 6a5 5 0 0 1 10-1 5 5 0 0 1 10 1c0 5.5-10 12-10 12z" fill="none" stroke="#888" stroke-width="1.3"/></svg>
      <span>WISHLIST</span>
    </div>
    <div class="site-tools tool--cart">
      <svg width="22" height="19" viewBox="0 0 22 19"><path d="M1 1h4l3 11h10l2-8H6" fill="none" stroke="#888" stroke-width="1.3"/><circle cx="9" cy="16" r="1.6" fill="#888"/><circle cx="17" cy="16" r="1.6" fill="#888"/></svg>
      <span>CART (0)</span>
    </div>

    <nav class="site-nav">
      <span class="site-nav__item" style="width:144px">FINE JEWELRY</span>
      <span class="site-nav__item" style="width:126px">TIMEPIECES</span>
      <span class="site-nav__item" style="width:139px">ACCESSORIES</span>
      <span class="site-nav__item" style="width:124px">DESIGNERS</span>
      <span class="site-nav__item" style="width:76px">SALE</span>
    </nav>
  </header>

  <section class="banner banner--inpage">
    <div class="banner__tree" role="img" aria-label="Photo of a lit, decorated Christmas tree by a window"></div>
    <div class="banner__panel">
      <h2 class="banner__headline">Christmas is closer</h2>
      <div class="banner__piece piece--earrings" role="img" aria-label="Product photo: pair of gemstone earrings"></div>
      <div class="banner__piece piece--cluster-ring" role="img" aria-label="Product photo: cabochon cluster ring"></div>
      <div class="banner__piece piece--scale-ring" role="img" aria-label="Product photo: textured gold band ring"></div>
      <div class="banner__piece piece--brooch" role="img" aria-label="Product photo: floral gold brooch"></div>
      <div class="banner__button button--think">THINK SALE !</div>
      <div class="banner__button button--shop">SHOP NOW</div>
    </div>
    <div class="banner__band">Thank You</div>
  </section>

  <section class="arrivals">
    <div class="arrivals__bar">NEW ARRIVALS
      <span class="arrivals__view-all">VIEW ALL</span>
    </div>
  </section>

</div>
</body>
</html>
```